Business cards

Design business cards for our company. Just a straight, business like design with the logo, name, function and contact details

Target Market(s)

We are a innovative technological company active in water treatment

Industry/Entity Type

Water management

Contact Information for Business Card

Name, Function, email, telephone number, link to website

```html
<!DOCTYPE html>
<html lang="en">
<head>
<meta charset="utf-8">
<title>Calvora – Business Cards</title>
<link rel="stylesheet" href="https://fonts.googleapis.com/css2?family=Arimo:wght@400;700&display=swap">
<style>
  :root {
    --backdrop: #e9e9e9;
    --card: #333333;
    --card-edge: #2b2b2b;
    --accent: #2f8fd6;
    --ink: #ffffff;
    --muted: #d8d8d8;
  }
  * { box-sizing: border-box; margin: 0; padding: 0; }
  html, body {
    width: 1200px;
    height: 802px;
    overflow: hidden;
    background: var(--backdrop);
    font-family: "Arimo", Arial, sans-serif;
  }
  .sheet {
    position: relative;
    width: 1200px;
    height: 802px;
  }
  .card {
    position: absolute;
    top: 258px;
    width: 500px;
    height: 286px;
    background: var(--card);
    border: 1px solid var(--card-edge);
    box-shadow: 0 10px 24px rgba(0,0,0,0.18);
    overflow: hidden;
  }
  .card--front { left: 70px; }
  .card--back  { left: 630px; }

  .corner-tab {
    position: absolute;
    top: 0;
    right: 34px;
    width: 22px;
    height: 16px;
    background: var(--accent);
  }
  .holder {
    position: absolute;
    top: 34px;
    right: 34px;
    text-align: right;
  }
  .holder__name {
    color: var(--accent);
    font-weight: 700;
    font-size: 17px;
    letter-spacing: 0.5px;
  }
  .holder__role {
    color: var(--ink);
    font-size: 13px;
    margin-top: 3px;
  }
  .brand {
    position: absolute;
    display: flex;
    align-items: center;
    gap: 10px;
  }
  .brand__name {
    color: var(--accent);
    font-weight: 400;
    font-size: 40px;
    letter-spacing: 1px;
    line-height: 1;
  }
  .brand__dot {
    width: 14px;
    height: 14px;
    border-radius: 50%;
    background: var(--accent);
  }
  .card--front .brand { left: 34px; top: 112px; }
  .card--back .brand  { right: 40px; top: 160px; }
  .card--back .brand__name { font-size: 46px; }

  .contact {
    position: absolute;
    left: 34px;
    bottom: 26px;
    color: var(--ink);
    font-size: 12.5px;
    line-height: 1.5;
  }
  .contact__address { margin-bottom: 6px; }
  .contact__row {
    display: flex;
    align-items: center;
    gap: 8px;
  }
  .contact__icon { width: 11px; height: 11px; flex: none; }
</style>
</head>
<body>
<main class="sheet">

  <section class="card card--front" aria-label="Business card front">
    <span class="corner-tab"></span>

    <div class="holder">
      <p class="holder__name">DANIEL MOREAU</p>
      <p class="holder__role">Manager</p>
    </div>

    <div class="brand">
      <span class="brand__name">Calvora</span>
      <span class="brand__dot"></span>
    </div>

    <div class="contact">
      <p class="contact__address">Your Address<br>City, State, Zip 0000</p>
      <p class="contact__row">
        <svg class="contact__icon" viewBox="0 0 12 12" aria-hidden="true">
          <path d="M2.5 1 L4.5 1 L5.3 3.6 L4 4.6 Q5 7 7.4 8 L8.4 6.7 L11 7.5 L11 9.5 Q10.5 11 9 11 Q1 10 1 3 Q1 1.5 2.5 1 Z" fill="var(--accent)"/>
        </svg>
        123-456-2100
      </p>
      <p class="contact__row">
        <svg class="contact__icon" viewBox="0 0 12 12" aria-hidden="true">
          <rect x="0.8" y="2.2" width="10.4" height="7.6" fill="none" stroke="var(--accent)" stroke-width="1.3"/>
          <path d="M1 2.6 L6 6.6 L11 2.6" fill="none" stroke="var(--accent)" stroke-width="1.3"/>
        </svg>
        contact@calvora-water.com
      </p>
      <p class="contact__row">
        <svg class="contact__icon" viewBox="0 0 12 12" aria-hidden="true">
          <circle cx="6" cy="6" r="5" fill="none" stroke="var(--accent)" stroke-width="1.2"/>
          <ellipse cx="6" cy="6" rx="2.2" ry="5" fill="none" stroke="var(--accent)" stroke-width="1"/>
          <path d="M1 6 H11 M2 3.5 H10 M2 8.5 H10" stroke="var(--accent)" stroke-width="0.9"/>
        </svg>
        www.calvora-water.com
      </p>
    </div>
  </section>

  <section class="card card--back" aria-label="Business card back">
    <div class="brand">
      <span class="brand__name">Calvora</span>
      <span class="brand__dot"></span>
    </div>
  </section>

</main>
</body>
</html>
```